FREE Network Assessment image for landing page

This graphic will be on a landing page and on the left will be Text and a download button that we change and control. The graphic for this project will be to the right.
I will add an example of the landing page area so that it makes more sense.

Please include the text from the sample - the font needs to be the same style as what we are using on the left side!

The graphic needs to be a .png file, roughly 713 x 527 white background. Use discretion on design layout.

Colors are black, Red = PMS 1795 and Gray = Cool Gray 10

Thanks,
Tom Harwick

Target Market(s)

small businesses

Industry/Entity Type

Information Technology

Font styles to use
Other font styles liked:
• See sample

Requirements
Must have
• see description
Nice to have
• Possibly small technology related image to help enhance the text but I don't want any image to compete with the text. Keep in mind the colors mentioned in the description - this is the web site colors.
Should not have
• Should not be hard to read

```html
<!DOCTYPE html>
<html lang="en">
<head>
<meta charset="utf-8">
<title>Free Network Health Assessment Tool</title>
<link href="https://fonts.googleapis.com/css2?family=Oswald:wght@300;400;500&family=Lato:wght@400&family=Open+Sans:wght@400&display=swap" rel="stylesheet">
<style>
  :root {
    --red: #e03134;
    --red-soft: #ee4a4c;
    --tab-gray: #646163;
    --heading-gray: #444446;
    --white: #ffffff;
    --art-red: #d9343a;
    --art-gray: #8a8a8c;
    --art-teal: #2a97a6;
  }
  html, body {
    margin: 0;
    padding: 0;
    width: 1200px;
    height: 1000px;
    overflow: hidden;
    background: var(--white);
  }
  .canvas {
    position: relative;
    width: 1200px;
    height: 1000px;
    background: var(--white);
  }
  .main-nav {
    position: absolute;
    left: 45px;
    top: 272px;
    width: 572px;
    height: 54px;
    background: var(--red);
    border-radius: 4px 0 0 4px;
    box-shadow: 0 4px 8px rgba(0,0,0,0.18);
    display: flex;
    padding-left: 66px;
    box-sizing: border-box;
  }
  .nav-item {
    font-family: 'Oswald', sans-serif;
    font-weight: 500;
    font-size: 14px;
    letter-spacing: 0.3px;
    color: var(--white);
    line-height: 54px;
    padding: 0 22px;
    text-transform: uppercase;
    display: flex;
    align-items: center;
  }
  .nav-item.is-active {
    background: var(--tab-gray);
    width: 78px;
    padding: 0;
    justify-content: center;
  }
  .nav-item svg { margin-left: 7px; }
  .offer-banner {
    position: absolute;
    left: 588px;
    top: 272px;
    width: 538px;
    height: 54px;
    background: var(--red);
    color: var(--white);
    font-family: 'Open Sans', sans-serif;
    font-size: 20px;
    display: flex;
    align-items: center;
    justify-content: center;
    padding-top: 4px;
    box-sizing: border-box;
  }
  .hero-title {
    position: absolute;
    left: 45px;
    top: 404px;
    margin: 0;
    font-family: 'Oswald', sans-serif;
    font-weight: 300;
    font-size: 55px;
    line-height: 67px;
    color: var(--heading-gray);
    letter-spacing: 0.2px;
  }
  .hero-lead {
    position: absolute;
    left: 45px;
    top: 566px;
    width: 590px;
    margin: 0;
    font-family: 'Lato', sans-serif;
    font-size: 19.5px;
    line-height: 27px;
    color: var(--red-soft);
  }
  .cta-button {
    position: absolute;
    left: 45px;
    top: 640px;
    width: 206px;
    height: 42px;
    background: var(--red-soft);
    border-radius: 21px;
    color: var(--white);
    font-family: 'Oswald', sans-serif;
    font-weight: 400;
    font-size: 15px;
    text-transform: uppercase;
    display: flex;
    align-items: center;
    justify-content: center;
    text-decoration: none;
  }
  .hero-art {
    position: absolute;
    left: 718px;
    top: 355px;
    width: 368px;
    height: 350px;
    border-radius: 50%;
    background: radial-gradient(circle at 50% 45%, var(--art-red) 0%, #e57a7c 38%, #cfd3dc 70%, #e9eaef 100%);
  }
</style>
</head>
<body>
<div class="canvas">
  <nav class="main-nav">
    <span class="nav-item is-active">Home</span>
    <span class="nav-item">About</span>
    <span class="nav-item">Team</span>
    <span class="nav-item">What makes us different
      <svg width="8" height="6" viewBox="0 0 8 6"><path d="M1 1 L4 4 L7 1" stroke="#fff" stroke-width="1.6" fill="none"/></svg>
    </span>
  </nav>
  <div class="offer-banner">FREE Network &amp; Computer health check Service</div>

  <h1 class="hero-title">FREE NETWORK HEALTH<br>ASSESSMENT TOOL</h1>
  <p class="hero-lead">Let us show you how to find and get rid of computer and network slowness, security vulnerabilities and potential disasters.</p>
  <a class="cta-button" href="#">Make an appointment</a>

  <div class="hero-art" role="img" aria-label="Illustration of a red security shield surrounded by a router, padlock, tools, server stack, firewall, computer monitor and globe on a circular ring"></div>
</div>
</body>
</html>
```